We invest in Electric Vehicles and renewable energy - help sell us!

INTRO: We want a PowerPoint template / Master Presentation to be used to sell our company and first investment fund to professional investors and to present ourselves to businesses that will develop the infrastructure projects in which we will invest.

WHO WE ARE: We are a newly created investment advisory and fund management company specialised in sustainable mobility.

WHAT WE DO: We invest in infrastructure projects that provide electric vehicles, charging infrastructure (charging stations etc) and associated renewable energy generation services (eg solar panels on roof-tops and solar parks, wind energy). The users of the projects in which we invest are operators of vehicle fleets (taxis, buses, delivery, which may be for 2, 3 and 4 wheel vehicles from motorbikes through cars, vans, buses and trucks).

PURPOSE OF THE POWERPOINT: We are looking for a presentation (1) to sell our investment services to investors (to raise money) and (2) to present what we do to fleet operators and service providers who will develop the projects.

CONTENT: We need all of the usual front cover slide / content slide / intermediate divider-heading slide / slides that integrate the most common tables, charts and smart graphics / team slide / a variety of text slides / a testimonial slide / Example project slide / Final contact and Disclaimer text slide etc all customised to the design. We rely on your experience for providing the further standard formats and layouts that one might find in a high-quality financial sector corporate presentation deck.

VERSIONS: We want three versions of the slides where there are images (eg front and back covers, section breaks, testimonial slides..). The three could be themed eg (1) futuristic and/or abstract in the theme of our investment scope (2) Street themes with vehicles and people in developed and developing markets (3) a mix of aerial and land-based views of roads (4) more explicit around the types of infrastructure in which we invest (vehicles of different types, charging infrastructure, solar panels on industrial and commercial roof tops etc)

LOOK & FEEL: The presentation must be sleek, dynamic if sober, with a clean feel, it should project an image of clarity and confidence, but also elicit some emotional appeal (even if it is very subtle!) ... we are in the e-mobility sector after all! We have an existing logo (attached).

We have an existing website www.quorlane.capital (one day it will need an upgrade too!) it may serve as inspiration / allow you better to understand our activities!

SOME PICS THAT WE LIKE: for inspiration only (NON exhaustive!):

• https://www.frametidepool.com/video/stock/unrecognizable-highway-traffic-head-on-kdwpqzrmtxa42ufhe
• https://www.frametidepool.com/video/stock/new-york-city-streets-qw8mxr5
• https://www.frametidepool.com/video/stock/4k-time-lapse-of-traffic-speeding-on-a-straight-section-of-highway-during-an-evening-rush-hour-zk7wqe3
• https://www.frametidepool.com/video/stock/cinematic-urban-aerial-time-lapse-of-city-infrastructure-including-freeways-interstates-roads-streets-with-traffic-at-rush-hour-during-the-evening-mxtrwpkudzlcfqe4k
• https://www.frametidepool.com/video/stock/charging-of-electric-car-eco-energy-transport-and-power-supply-environmentally-conscious-transportation-vehicle-plugged-in-charger-terminal-in-the-city-4k-wvt3hdyxnacbzkfmee
• https://www.frametidepool.com/video/stock/drone-view-of-modern-vehicle-driving-on-road-near-ploughed-field-and-wind-turbine-in-countryside-hpxmbwtlcjr27nqeu

FINALLY: note the attached 'slides to include' are additonal slides that we want to be well presented (see additional detail on Slide 1 of the file)

Institutional investors (pension funds, asset managers, family offices) & the dreamer in each of us!!

Financial services (B2B NOT B2C)

• Calibri but can consider alternatives

• We need all of the usual front cover slide / content slide / intermediate divider-heading slide / slides that integrate the most common tables, charts and smart graphics / team slide / a variety of text slides / a testimonial slide / Example project slide / Final contact and Disclaimer text slide etc all customised to the design. We rely on your experience for providing the further standard formats and layouts that one might find in a high-quality financial sector corporate presentation deck
• Would like to see any other pages that are standard in your experience! Also would like to see one version of the slides with a summary section clearly marked for each slide (with space for text) which will serve for quick reading of the presentation for key points)

```html
<!DOCTYPE html>
<html lang="en">
<head>
<meta charset="utf-8">
<title>Quorlane Capital — Presentation Master</title>
<link href="https://fonts.googleapis.com/css2?family=Fira+Sans:wght@400;500;600&display=swap" rel="stylesheet">
<style>
:root{
  --green-dark:#2a4220;
  --green-deep:#27461d;
  --green:#6f9e3c;
  --grey-bg:#e8e8e8;
  --ink:#222;
  --white:#fff;
  --page:#fff;
}
*{box-sizing:border-box;margin:0;padding:0}
html,body{width:1200px;height:3654px;overflow:hidden;background:var(--page);font-family:"Fira Sans",sans-serif;color:var(--ink)}
.slide{position:absolute;left:99px;width:997px;height:561px;overflow:hidden}
.s1{top:56px}.s2{top:645px}.s3{top:1238px}.s4{top:1831px}.s5{top:2426px}.s6{top:3023px}
.photo{position:absolute;inset:0}
.wordmark{font-family:"Fira Sans",sans-serif;font-weight:500;color:var(--white);white-space:nowrap;letter-spacing:.5px}
.wordmark.dark{color:var(--green-deep)}
.corner-mark{position:absolute;right:16px;bottom:12px;font-size:24px}
/* cover */
.s1 .photo{background:linear-gradient(180deg,#b8602e 0%,#9a5a34 30%,#5f5a52 65%,#3d4858 100%)}
.s1 .shade{position:absolute;inset:0;background:radial-gradient(ellipse at 60% 20%,rgba(255,190,110,.35),transparent 60%)}
.cover-mark{position:absolute;top:170px;width:100%;text-align:center;font-size:66px}
.cover-title{position:absolute;top:282px;width:100%;text-align:center;color:var(--white);font-size:44px;font-weight:600;line-height:56px;letter-spacing:.5px}
/* about */
.s2{background:var(--green-dark)}
.s2 .photo{left:537px;background:linear-gradient(180deg,#3a4f7a 0%,#6f7898 35%,#1d2430 60%,#7a2a22 80%,#2a1a18 100%)}
.about-box{position:absolute;left:56px;top:137px;width:575px;height:287px;background:var(--green);padding:22px 20px}
.about-box h2{color:var(--white);font-size:41px;font-weight:500;margin-bottom:8px}
.about-box p{color:var(--white);font-size:15px;line-height:33px}
/* projects */
.s3,.s4{background:var(--grey-bg)}
.s3 h2,.s4 h2{position:absolute;width:100%;text-align:center;color:var(--green-deep);font-weight:600;font-size:40px}
.s3 h2{top:36px}
.s3 .lede{position:absolute;top:100px;width:100%;text-align:center;font-size:15px}
.s3 .photo{left:31px;top:155px;width:442px;height:347px;background:linear-gradient(160deg,#6f7c8a,#3b7a8c 40%,#7a7a62 70%,#4a4a44)}
.proj-col{position:absolute;left:501px;top:150px;width:470px}
.proj-col h3{color:var(--green);font-size:26px;font-weight:500;line-height:35px}
.proj-col .intro{font-size:13px;font-weight:600;margin:10px 0 14px}
.proj-col ul{list-style:none}
.proj-col li{position:relative;padding-left:18px;font-size:11.5px;line-height:21px;margin-bottom:10px}
.proj-col li svg{position:absolute;left:0;top:4px}
/* chart */
.s4 h2{top:38px}
.chart{position:absolute;left:0;top:0}
/* team */
.s5 .photo{background:linear-gradient(120deg,#3a3a3a,#1e1e1e 50%,#303030)}
.s5 h2{position:absolute;top:40px;width:100%;text-align:center;color:var(--white);font-size:46px;font-weight:600}
.s5 .lede{position:absolute;top:112px;left:115px;right:115px;text-align:center;color:var(--white);font-size:16.5px;line-height:32px}
.card{position:absolute;top:232px;width:209px;height:275px;background:var(--white);text-align:center;padding-top:22px}
.card .portrait{width:127px;height:127px;border-radius:50%;margin:0 auto 12px;background:linear-gradient(160deg,#9aa3ad,#4a4f55)}
.card h4{font-size:16px;font-weight:500;color:var(--green-deep)}
.card .role{font-size:12px;color:var(--green);font-weight:500;margin:3px 0 8px}
.card p{font-size:8.5px;line-height:17px;padding:0 20px}
/* thanks */
.s6 .photo{background:linear-gradient(180deg,#5a4e42 0%,#3e3a36 40%,#2a2c30 70%,#1e2024 100%)}
.s6 h2{position:absolute;top:110px;width:100%;text-align:center;color:var(--white);font-size:44px;font-weight:600}
.s6 .lede{position:absolute;top:180px;left:80px;right:80px;text-align:center;color:var(--white);font-size:17px;line-height:32px}
.thanks-mark{position:absolute;top:278px;width:100%;text-align:center;font-size:66px}
.contacts{position:absolute;top:385px;left:160px;display:flex;align-items:center;gap:20px;color:var(--white);font-size:13px;font-weight:500}
.contacts .item{display:flex;align-items:center;gap:12px;margin-right:20px;line-height:20px}
.contacts .icon{width:54px;height:54px;border-radius:50%;background:var(--green);border:3px solid var(--white);display:flex;align-items:center;justify-content:center}
</style>
</head>
<body>

<section class="slide s1">
  <div class="photo" role="img" aria-label="Sunset highway traffic seen from the roadside"></div>
  <div class="shade"></div>
  <div class="wordmark cover-mark">Quorlane Capital</div>
  <h1 class="cover-title">Project finance to scale electric<br>vehicles, globally</h1>
</section>

<section class="slide s2">
  <div class="photo" role="img" aria-label="Dusk time-lapse of light trails on a highway through trees"></div>
  <div class="about-box">
    <h2>About Quorlane Capital</h2>
    <p>Quorlane Capital S.A. is a yet-to-be established investment advisory and management company. The company was founded in early 2020 in recognition of the growing need for, and opportunity that lies within, sustainable transport. Quorlane Capital was selected for the Spring 2020 cohort of the Northvale Clean Transport Accelerator.</p>
  </div>
  <div class="wordmark corner-mark">Quorlane Capital</div>
</section>

<section class="slide s3">
  <h2>Projects</h2>
  <p class="lede">We provide project financing to enable owners and operators of commercial fleets to adopt cleaner technologies.</p>
  <div class="photo" role="img" aria-label="Busy city street with colourful buses and pedestrians"></div>
  <div class="proj-col">
    <h3>What types of projects do<br>we invest in?</h3>
    <p class="intro">We invest in projects with the following characteristics:</p>
    <ul>
      <li><svg width="12" height="12" viewBox="0 0 12 12"><circle cx="6" cy="6" r="5" fill="none" stroke="#6f9e3c"/><path d="M3.5 6.2l1.7 1.6 3.3-3.4" fill="none" stroke="#6f9e3c" stroke-width="1.2"/></svg>The project enables owners and operators of commercial fleets (such as buses, trucks, taxis) to reduce or avoid emissions by the adoption of cleaner technologies. This could include the purchase of plug-in electric or hydrogen vehicles, the retrofitting of existing vehicles, and the installation of charging infrastructure</li>
      <li><svg width="12" height="12" viewBox="0 0 12 12"><circle cx="6" cy="6" r="5" fill="none" stroke="#6f9e3c"/><path d="M3.5 6.2l1.7 1.6 3.3-3.4" fill="none" stroke="#6f9e3c" stroke-width="1.2"/></svg>The project has a high climate and health impact potential, and a measurable impact at city and regional levels</li>
      <li><svg width="12" height="12" viewBox="0 0 12 12"><circle cx="6" cy="6" r="5" fill="none" stroke="#6f9e3c"/><path d="M3.5 6.2l1.7 1.6 3.3-3.4" fill="none" stroke="#6f9e3c" stroke-width="1.2"/></svg>The project aligns with our investment principles, and our environmental management systems</li>
      <li><svg width="12" height="12" viewBox="0 0 12 12"><circle cx="6" cy="6" r="5" fill="none" stroke="#6f9e3c"/><path d="M3.5 6.2l1.7 1.6 3.3-3.4" fill="none" stroke="#6f9e3c" stroke-width="1.2"/></svg>The project is expected to provide attractive financial return</li>
    </ul>
  </div>
  <div class="wordmark dark corner-mark">Quorlane Capital</div>
</section>

<section class="slide s4">
  <h2>Nemo enim ipsam voluptatem</h2>
  <svg class="chart" width="997" height="561" viewBox="0 0 997 561" font-family="Fira Sans, sans-serif" font-size="12" font-weight="600" fill="#222">
    <g stroke="#c8c8c8" stroke-width="1">
      <line x1="184" x2="850" y1="133" y2="133"/><line x1="184" x2="850" y1="169" y2="169"/>
      <line x1="184" x2="850" y1="206" y2="206"/><line x1="184" x2="850" y1="242" y2="242"/>
      <line x1="184" x2="850" y1="278" y2="278"/><line x1="184" x2="850" y1="315" y2="315"/>
      <line x1="184" x2="850" y1="351" y2="351"/><line x1="184" x2="850" y1="387" y2="387"/>
      <line x1="184" x2="850" y1="424" y2="424"/>
    </g>
    <line x1="184" x2="184" y1="133" y2="460" stroke="#888"/>
    <line x1="184" x2="850" y1="460" y2="460" stroke="#888"/>
    <g text-anchor="end">
      <text x="176" y="137">800</text><text x="176" y="173">600</text><text x="176" y="210">400</text>
      <text x="176" y="246">200</text><text x="176" y="282">100</text><text x="176" y="319">80</text>
      <text x="176" y="355">60</text><text x="176" y="391">40</text><text x="176" y="428">20</text>
      <text x="176" y="464">0</text>
    </g>
    <g>
      <rect x="194" y="435" width="24" height="25" fill="#6f9e3c"/>
      <rect x="263" y="278" width="24" height="182" fill="#6f9e3c"/>
      <rect x="332" y="134" width="24" height="326" fill="#000"/>
      <rect x="401" y="278" width="24" height="182" fill="#6f9e3c"/>
      <rect x="471" y="242" width="24" height="218" fill="#000"/>
      <rect x="541" y="242" width="24" height="218" fill="#6f9e3c"/>
      <rect x="610" y="151" width="24" height="309" fill="#000"/>
      <rect x="680" y="242" width="24" height="218" fill="#6f9e3c"/>
      <rect x="750" y="206" width="24" height="254" fill="#000"/>
      <rect x="821" y="260" width="24" height="200" fill="#6f9e3c"/>
    </g>
    <g text-anchor="middle">
      <text x="206" y="482">2012</text><text x="275" y="482">2013</text><text x="344" y="482">2014</text>
      <text x="413" y="482">2015</text><text x="483" y="482">2016</text><text x="553" y="482">2017</text>
      <text x="622" y="482">2018</text><text x="692" y="482">2019</text><text x="762" y="482">2020</text>
      <text x="833" y="482">2021</text>
    </g>
  </svg>
  <div class="wordmark dark corner-mark">Quorlane Capital</div>
</section>

<section class="slide s5">
  <div class="photo" role="img" aria-label="Dimmed photo of colleagues talking in an office"></div>
  <h2>Our Team</h2>
  <p class="lede">Sed ut perspiciatis unde omnis iste natus error sit voluptatem accusantium doloremque laudantium, totam rem aperiam, eaque ipsa quae ab illo inventore veritatis et quasi architecto beatae vitae dicta sunt explicabo</p>
  <div class="card" style="left:41px"><div class="portrait" role="img" aria-label="Portrait of Arden Halvik"></div><h4>Arden Halvik</h4><div class="role">Partner</div><p>Sed ut perspiciatis unde omnis iste natus error sit voluptatem accusantium dolo enim ipsam voluptatem quia.</p></div>
  <div class="card" style="left:277px"><div class="portrait" role="img" aria-label="Portrait of Kenji Orimura" style="background:linear-gradient(180deg,#7a8fa8,#4a5560 60%,#3a2a2a)"></div><h4>Kenji Orimura</h4><div class="role">Partner</div><p>Sed ut perspiciatis unde omnis iste natus error sit voluptatem accusantium dolo enim ipsam voluptatem quia.</p></div>
  <div class="card" style="left:512px"><div class="portrait" role="img" aria-label="Portrait of Dario Vassend" style="background:linear-gradient(160deg,#5a4a40,#1e1e1e)"></div><h4>Dario Vassend</h4><div class="role">Partner</div><p>Sed ut perspiciatis unde omnis iste natus error sit voluptatem accusantium dolo enim ipsam voluptatem quia.</p></div>
  <div class="card" style="left:748px"><div class="portrait" role="img" aria-label="Portrait of Maren Colbeck" style="background:linear-gradient(160deg,#d8d8d8,#b8a488)"></div><h4>Maren Colbeck</h4><div class="role">Consultant</div><p>Sed ut perspiciatis unde omnis iste natus error sit voluptatem accusantium dolo enim ipsam voluptatem quia.</p></div>
  <div class="wordmark corner-mark">Quorlane Capital</div>
</section>

<section class="slide s6">
  <div class="photo" role="img" aria-label="Dimmed city street with moving traffic at dusk"></div>
  <h2>Thank You!</h2>
  <p class="lede">Sed ut perspiciatis unde omnis iste natus error sit voluptatem accusantium doloremque laudantium, totam rem aperiam, eaque ipsa quae ab illo inventore.</p>
  <div class="wordmark thanks-mark">Quorlane Capital</div>
  <div class="contacts">
    <div class="item"><span class="icon"><svg width="20" height="24" viewBox="0 0 20 24"><path d="M10 1a8 8 0 0 0-8 8c0 6 8 14 8 14s8-8 8-14a8 8 0 0 0-8-8z" fill="#fff"/><circle cx="10" cy="9" r="3" fill="#6f9e3c"/></svg></span><span>Sed ut perspiciatis unde<br>omnis iste natus</span></div>
    <div class="item"><span class="icon"><svg width="22" height="22" viewBox="0 0 24 24"><path d="M6.6 10.8a15 15 0 0 0 6.6 6.6l2.2-2.2a1 1 0 0 1 1-.25 11.4 11.4 0 0 0 3.6.57 1 1 0 0 1 1 1V20a1 1 0 0 1-1 1A17 17 0 0 1 3 4a1 1 0 0 1 1-1h3.5a1 1 0 0 1 1 1c0 1.25.2 2.450.57 3.57a1 1 0 0 1-.25 1z" fill="#fff"/></svg></span><span>1-800-555-0142</span></div>
    <div class="item"><span class="icon"><svg width="24" height="18" viewBox="0 0 24 18"><rect x="1" y="1" width="22" height="16" rx="2" fill="#fff"/><path d="M2 2l10 8 10-8" fill="none" stroke="#6f9e3c" stroke-width="2"/></svg></span><span>info@quorlane.capital</span></div>
  </div>
  <div class="wordmark corner-mark">Quorlane Capital</div>
</section>

</body>
</html>
```